Halvard Atelier Business cards

Design our business cards and eventually a logo. The company is based in Paris, its activity is the retailing via internet of luxury home furniture (like Vambrelli, Bercusa, tarvoni...) Our clients are international andwith a high sense of aesthetics. The design shall communicate wealth and trust with a high quality and aesthetic sense, pure lines Company Name is Halvard AtelierExplanation of the name: usually people who wants to buy furniture usually go in a showroom. Today they go in showroom to test the furniture and they search for the price on internet, which is a "Halvard atelier".We will not be a e-commerce site. Our site will be (another project) a presentation site which purpose is to reach qualified prospects. Then everything will be handled by phone, meeting etc.The business card must be professional as we will negotiate with many luxury brands, opportunity to represent them on our site, prices etc.As far as the color are concerned mostly black and whithe or grey. The font of the Halvard Atelier name shall have some impact.

Target Market(s)

High-end furniture and buyers of luxury goods, international customers, mostly women who handle such projects.
We also deal with professional buyers (hotels as an example) and luxury brands

Contact Information for Business Card

standard format 85x55, lanscape card, square corners will be printed on thick high quality paper (300 or 350g)

Font styles to use
Sans Serif

Colors

Designer to choose colors to be used in the design.

Requirements
Must have
• Must be white, as the paper will be high quality, the paper will enhance the card.
• Name of the brand Halvard atelier (with specific font which make it very nice looking and catch the attention. similar to Calibri or Calibri
• Name of person (will give you the name later (4 names and position)
• the position of the person
• Mobile phone, e-mail, Physical address 27, rue Fenouillard, 75005 Paris, France (courrier only) our web site www.halvardatelier.fr
• The card must be simple and class
Nice to have
• Font of the address is smaller than the rest,
• Calibri font or similar on recto side with the name of the company which may look similar to the picture inserted in the brief.
• The grey color in the picture inserted is ok for us
Should not have
• Any parallel lines which represent the name of the company
• Any heavy design If you go on internet sites which present the furniture all designs are pure lines and high quality craftsmanship. To have an idea of our targetted client or brand we will be in touch: https://www.casavelumi.it/projects/
• Note that the picture added below is what we use, now as mail signature, up to you to have a better design etc.

```html
<!DOCTYPE html>
<html lang="en">
<head>
<meta charset="utf-8">
<title>Halvard Atelier — Business Cards</title>
<link href="https://fonts.googleapis.com/css2?family=Open+Sans:wght@400;600&family=Noto+Serif:ital@1&display=swap" rel="stylesheet">
<style>
  :root {
    --backdrop: #cfd0d2;
    --paper: #f7f7f6;
    --ink: #3c3c3e;
    --brand-grey: #59595b;
    --accent-blue: #3f8dd2;
    --band-grey: #58585a;
    --card-dark: #3a3a3c;
    --dark-logo: #9b9b9d;
  }
  * { margin: 0; padding: 0; box-sizing: border-box; }
  html, body { width: 1200px; height: 943px; overflow: hidden; }
  body {
    background: var(--backdrop);
    font-family: "Open Sans", Arial, sans-serif;
    position: relative;
  }
  .card {
    position: absolute;
    width: 510px;
    height: 330px;
    box-shadow: 0 10px 24px rgba(0,0,0,0.22);
    overflow: hidden;
  }
  .card--front { left: 55px; top: 150px; background: var(--paper); }
  .card--back  { left: 635px; top: 150px; background: var(--card-dark); }

  .brand-name {
    font-weight: 600;
    letter-spacing: 0.04em;
    text-transform: uppercase;
    white-space: nowrap;
  }
  .card--front .brand-name {
    position: absolute; left: 40px; top: 70px;
    font-size: 26px; color: var(--brand-grey);
  }
  .card--back .brand-name {
    position: absolute; left: 0; right: 0; top: 140px;
    text-align: center; font-size: 30px; color: var(--dark-logo);
  }

  .front-band { position: absolute; left: 0; bottom: 0; width: 100%; height: 42px; }

  .contact {
    position: absolute; left: 290px; top: 150px;
    color: var(--ink);
  }
  .contact__name { font-size: 21px; font-weight: 600; color: var(--ink); line-height: 1.1; }
  .contact__role {
    font-family: "Noto Serif", Georgia, serif; font-style: italic;
    font-size: 13px; color: var(--accent-blue); margin-bottom: 8px;
  }
  .contact__line { display: flex; align-items: flex-start; gap: 7px; font-size: 12.5px; line-height: 1.4; }
  .contact__line svg { flex: none; margin-top: 3px; }
  .contact__address { font-size: 12px; }

  .logo-lockup {
    position: absolute; left: 700px; top: 770px;
    display: flex; align-items: center; gap: 14px;
  }
  .logo-lockup__dot { width: 14px; height: 14px; background: var(--accent-blue); }
  .logo-lockup .brand-name { font-size: 34px; color: var(--brand-grey); }
</style>
</head>
<body>

  <section class="card card--front" aria-label="Business card, front">
    <div class="brand-name">Halvard Atelier</div>

    <div class="contact">
      <div class="contact__name">Mathis Delorme</div>
      <div class="contact__role">Président and Co-Founder</div>
      <div class="contact__line">
        <svg width="11" height="11" viewBox="0 0 12 12" aria-hidden="true"><path d="M2 1h2.5l1 3-1.5 1a7 7 0 0 0 3 3l1-1.5 3 1V10a1.5 1.5 0 0 1-1.5 1.5A9.5 9.5 0 0 1 .5 2.5 1.5 1.5 0 0 1 2 1z" fill="var(--accent-blue)"/></svg>
        <span>+33641279058</span>
      </div>
      <div class="contact__line contact__address">
        <svg width="11" height="12" viewBox="0 0 12 14" aria-hidden="true"><path d="M6 0a5 5 0 0 0-5 5c0 3.8 5 9 5 9s5-5.2 5-9a5 5 0 0 0-5-5zm0 7a2 2 0 1 1 0-4 2 2 0 0 1 0 4z" fill="var(--accent-blue)"/></svg>
        <span>27, rue Fenouillard<br>75005 Paris, France</span>
      </div>
    </div>

    <svg class="front-band" viewBox="0 0 510 42" preserveAspectRatio="none" aria-hidden="true">
      <polygon points="0,0 385,0 400,42 0,42" fill="var(--accent-blue)"/>
      <polygon points="385,0 510,0 510,42 400,42" fill="var(--band-grey)"/>
    </svg>
  </section>

  <section class="card card--back" aria-label="Business card, back">
    <div class="brand-name">Halvard Atelier</div>
  </section>

  <div class="logo-lockup">
    <span class="logo-lockup__dot"></span>
    <span class="brand-name">Halvard Atelier</span>
  </div>

</body>
</html>
```